Stationery Design Project

We are looking stationary Design for Velbrook International, a high end clothing company. I have attached an image of our Logo below.
Updates
I am looking for designs for the following stationaries:
1. Leather Binders
2. Paper Binders
3. Letterhead
4. Envelopes
5. Pens, pencils etc
We would love to see designs with gold, black and white color combination.
Industry/Entity Type
Clothing
Look and feel
Each slider illustrates characteristics of the customer's brand and the style your logo design should communicate.

```html
<!DOCTYPE html>
<html lang="en">
<head>
<meta charset="utf-8">
<title>Velbrook International — Stationery</title>
<link rel="stylesheet" href="https://fonts.googleapis.com/css2?family=Montserrat:wght@400;500&display=swap">
<style>
  :root {
    --ink: #0b0b0b;
    --paper: #ffffff;
    --stage: #e6e6e6;
    --rule: #d0d0d0;
    --soft: #9a9a9a;
  }
  * { margin: 0; padding: 0; box-sizing: border-box; }
  html, body { width: 1200px; height: 467px; overflow: hidden; }
  body {
    background: var(--stage);
    font-family: "Montserrat", Arial, sans-serif;
    position: relative;
  }
  .piece { position: absolute; box-shadow: 0 2px 6px rgba(0,0,0,.18); }

  .wordmark {
    font-family: "Montserrat", Arial, sans-serif;
    font-weight: 500;
    text-transform: uppercase;
    letter-spacing: .18em;
    text-align: center;
    line-height: 1.5;
  }
  .mark-dot {
    display: block;
    margin: 0 auto 8px;
    border-radius: 50%;
    border: 1px solid currentColor;
  }

  /* Paper binder cover */
  .paper-binder {
    left: 40px; top: 22px; width: 495px; height: 190px;
    background: var(--paper);
  }
  .paper-binder .wordmark {
    position: absolute; left: 0; right: 0; top: 36px;
    color: var(--ink); font-size: 13px;
  }
  .paper-binder .mark-dot { width: 26px; height: 26px; }
  .paper-binder .band {
    position: absolute; left: 0; right: 0; top: 124px; height: 26px;
    background: var(--ink);
  }

  /* Leather binder cover */
  .leather-binder {
    left: 40px; top: 244px; width: 495px; height: 200px;
    background: var(--ink);
  }
  .leather-binder .wordmark {
    position: absolute; left: 0; right: 0; top: 50px;
    color: #cfcfcf; font-size: 15px;
  }
  .leather-binder .mark-dot { width: 32px; height: 32px; }
  .leather-binder .spine {
    position: absolute; left: 0; top: 0; bottom: 0; width: 8px;
    background: #1c1c1c;
  }

  /* Letterhead */
  .letterhead {
    left: 600px; top: 50px; width: 262px; height: 370px;
    background: var(--paper);
  }
  .letterhead .tab {
    position: absolute; left: 16px; top: 0; width: 30px; height: 30px;
    background: var(--ink); color: var(--paper);
    font-size: 4px; display: flex; align-items: center; justify-content: center;
  }

  /* Envelopes */
  .envelope { left: 885px; width: 290px; background: var(--ink); }
  .envelope-back { top: 28px; height: 120px; }
  .envelope-back svg { position: absolute; inset: 0; }
  .envelope-front { top: 165px; height: 110px; }
  .envelope-front .tab {
    position: absolute; right: 10px; bottom: 10px; width: 38px; height: 38px;
    background: var(--paper); color: var(--ink);
    font-size: 4.5px; display: flex; align-items: center; justify-content: center;
  }

  /* Business cards */
  .card { top: 300px; width: 140px; height: 82px; }
  .card-front { left: 885px; background: var(--ink); color: var(--paper); }
  .card-front .tab {
    position: absolute; left: 8px; top: 14px; width: 30px; height: 30px;
    background: var(--paper); color: var(--ink);
    font-size: 3.5px; display: flex; align-items: center; justify-content: center;
  }
  .card-front .holder {
    position: absolute; left: 48px; top: 24px; font-size: 9px; font-weight: 400;
  }
  .card-back { left: 1035px; background: var(--paper); color: var(--ink); }
  .card-back .block {
    position: absolute; left: 0; top: 10px; width: 30px; height: 28px;
    background: var(--ink);
  }
  .card-back .contact {
    position: absolute; left: 10px; top: 44px; font-size: 6px; line-height: 1.35;
  }
  .card-back .contact .phone-alt { position: absolute; left: 78px; top: 8px; white-space: nowrap; }
</style>
</head>
<body>

  <section class="piece paper-binder" aria-label="Paper binder cover">
    <div class="wordmark"><span class="mark-dot"></span>Velbrook<br>International</div>
    <div class="band"></div>
  </section>

  <section class="piece leather-binder" aria-label="Leather binder cover">
    <div class="spine"></div>
    <div class="wordmark"><span class="mark-dot"></span>Velbrook<br>International</div>
  </section>

  <section class="piece letterhead" aria-label="Letterhead">
    <div class="tab wordmark">Velbrook</div>
  </section>

  <section class="piece envelope envelope-back" aria-label="Envelope, flap side">
    <svg width="290" height="120" viewBox="0 0 290 120">
      <polyline points="0,0 145,58 290,0" fill="none" stroke="#2a2a2a" stroke-width="1"/>
    </svg>
  </section>

  <section class="piece envelope envelope-front" aria-label="Envelope, front">
    <div class="tab wordmark">Velbrook</div>
  </section>

  <section class="piece card card-front" aria-label="Business card, front">
    <div class="tab wordmark">Velbrook</div>
    <p class="holder">Clara Weston</p>
  </section>

  <section class="piece card card-back" aria-label="Business card, back">
    <div class="block"></div>
    <div class="contact">
      <p>Av. Lumen 218</p>
      <p>2314 560 781</p>
      <p>clara@velbrook.com</p>
      <p class="phone-alt">088 612 907</p>
    </div>
  </section>

</body>
</html>
```